v eLiquid Label

We are an electronic cigarette eLiquid manufacturer with an outdated label design which needs to be updated and become more modern. All information listed on the label cannot be changed or removed.

There are 4 colour coding on the labels that cannot change.
0mg is white
12mg is yellow
18mg is blue
24mg is red

We prefer a blue type background however are not committed to it with the proper design however if a new colour is chosen it must compliment the colour band for each colour coding

The "dots" on the front of the bottle need to be larger.

The "V" on the front needs to be in this font however we can accept slight changes to it for effect.

Issues we are facing:
The 0mg and the 18mg look too close in colour and need to be completely different in colouring.

The background colouring is too dark and you cannot see the 50/50 in the watermark.

Reason: We have not received a design which is suitable to our needs. We have see a few close ones however not exact. Thanks

Reason: I was forced to go out of country for a family emergency and to be fair I am extending the deadline

```html
<!DOCTYPE html>
<html lang="en">
<head>
<meta charset="utf-8">
<title>VELA E-Liquid Label – Sweet Tobacco 24 mg/ml</title>
<link rel="stylesheet" href="https://fonts.googleapis.com/css2?family=Arimo:wght@400;700&family=Alfa+Slab+One&display=swap">
<style>
  :root {
    --band-red: #d9141b;
    --band-text: #ffffff;
    --ink: #111111;
    --paper-light: #f5f8fd;
    --paper-mid: #d3def2;
    --blue-soft: #7d9ad9;
    --blue-mid: #5379c9;
    --blue-core: #3d63b8;
    --white: #ffffff;
    --watermark: rgba(255,255,255,0.34);
    --watermark-edge: rgba(45,80,160,0.14);
  }
  * { margin: 0; padding: 0; box-sizing: border-box; }
  html, body { width: 1200px; height: 461px; overflow: hidden; background: #ffffff; }
  .label {
    position: relative; width: 1200px; height: 461px; overflow: hidden;
    font-family: "Arimo", Arial, sans-serif; color: var(--ink);
    background: linear-gradient(to right,
      var(--paper-light) 0%, var(--paper-mid) 24%, var(--blue-soft) 36%,
      var(--blue-mid) 43%, var(--blue-core) 50%, var(--blue-mid) 57%,
      var(--blue-soft) 64%, var(--paper-mid) 78%, var(--paper-light) 100%);
  }
  .band {
    position: absolute; left: 0; width: 1200px; height: 36px;
    background: var(--band-red); color: var(--band-text);
    font-weight: 700; line-height: 36px;
    display: flex; justify-content: space-between; white-space: nowrap; overflow: hidden;
    padding: 0 4px;
  }
  .band--strength { top: 0; font-size: 25px; }
  .band--strength span:last-child { margin-right: -40px; }
  .band--danger { bottom: 0; font-size: 28px; padding-left: 3px; }
  .band--danger span:last-child { margin-right: -8px; }

  .watermark {
    position: absolute; left: 0; top: 36px; width: 1200px; height: 389px;
    font-weight: 700; font-style: italic; font-size: 128px; line-height: 128px;
    color: var(--watermark); -webkit-text-stroke: 1.5px var(--watermark-edge);
    white-space: nowrap; pointer-events: none;
  }
  .watermark span { display: block; }

  .hazard-icon { position: absolute; left: 22px; top: 52px; width: 46px; height: 46px; }

  .panel { position: absolute; font-size: 18px; line-height: 25.8px; }
  .panel--fr { right: 808px; top: 49px; width: 400px; text-align: right; }
  .panel--en { left: 795px; top: 54px; width: 400px; }
  .panel h2 { font-size: 17px; font-weight: 700; }
  .panel strong, .panel .first-aid { font-weight: 700; }
  .panel--en .first-aid { margin-top: 27px; }

  .producer { position: absolute; font-size: 16px; line-height: 25px; }
  .producer--fr { right: 808px; top: 376px; width: 400px; text-align: right; }
  .producer--en { left: 791px; top: 376px; }

  .batch-box {
    position: absolute; left: 790px; top: 345px; width: 400px; height: 28px;
    background: var(--white); border: 1px solid #333;
    display: flex; align-items: center; font-size: 17px; padding: 0 6px;
  }
  .batch-box small { font-size: 10px; margin-right: 8px; }
  .batch-box .expiry { margin-left: auto; }

  .brand-name {
    position: absolute; left: 400px; top: 92px; width: 400px; text-align: center;
    font-weight: 700; font-size: 124px; line-height: 1; color: var(--white);
  }
  .strength-dot {
    position: absolute; left: 440px; top: 252px; width: 92px; height: 92px;
    border-radius: 50%; background: var(--band-red); border: 4px solid var(--white);
    color: var(--white); font-weight: 700; font-size: 40px;
    display: flex; align-items: center; justify-content: center;
  }
  .volume {
    position: absolute; left: 660px; top: 278px; color: var(--white);
    font-weight: 700; font-size: 28px;
  }
  .product-type {
    position: absolute; left: 612px; top: 312px; color: var(--white);
    font-family: "Alfa Slab One", Georgia, serif; font-size: 22px;
  }
  .flavour {
    position: absolute; left: 430px; top: 368px; width: 332px; text-align: center;
    color: var(--white); font-family: "Alfa Slab One", Georgia, serif; font-size: 30px;
  }
</style>
</head>
<body>
<main class="label">
  <div class="watermark" aria-hidden="true">
    <span style="margin-left:140px">/50 50/50 50/50 50/</span>
    <span style="margin-left:150px">50/50 50/50 50/50</span>
    <span style="margin-left:110px">50/50 50/50 50/50 5</span>
  </div>

  <div class="band band--strength">
    <span>24 mg/ml</span><span>24 mg/ml</span><span>24 mg/ml</span><span>24 mg/ml</span>
    <span>24 mg/ml</span><span>24 mg/ml</span><span>24 mg/ml</span><span>24 mg/ml</span>
  </div>

  <svg class="hazard-icon" viewBox="0 0 46 46" role="img" aria-label="Poison hazard symbol">
    <polygon points="14,2 32,2 44,14 44,32 32,44 14,44 2,32 2,14" fill="#ffffff" stroke="#111" stroke-width="2.5"/>
    <rect x="13" y="13" width="20" height="20" rx="4" fill="#555"/>
  </svg>

  <section class="panel panel--fr" lang="fr">
    <h2>CONTENIR NOCIF</h2>
    <p>Ne pas avaler.</p>
    <p>Ne pas mettre dans les yeux ou<br>sur la peau ou les vêtements.</p>
    <p>Tenir hors de portée des enfants et<br>des animaux.</p>
    <p><strong>INGRÉDIENTS:</strong> Propylène Glycol,<br>Glycérine, Alcool de Qualité Alimentaire,<br>Arômes Naturel et Artificiels.</p>
    <p class="first-aid">En cas d'ingestion consulter<br>centre antipoison ou un médecin<br>immédiatement. Peux contenir de noix.</p>
  </section>
  <p class="producer producer--fr" lang="fr">Produit et emballé exclusivement pour:<br>5132960 Maple Labs Inc, Ashford ON, K0B 3L0</p>

  <div class="brand-name">VELA</div>
  <div class="strength-dot">24</div>
  <div class="volume">30 ml</div>
  <div class="product-type">E-LIQUID</div>
  <div class="flavour">SWEET TOBACCO</div>

  <section class="panel panel--en">
    <h2>WARNING CONTENTS HARMFUL</h2>
    <p>Do not swallow.</p>
    <p>Do not get in eyes or on skin or clothing.</p>
    <p>Keep out of reach of children and pets.</p>
    <p><strong>INGREDIENTS:</strong> Propylene Glycol,<br>Vegetable Glycerin, Food Grade Alcohol,<br>Natural and Artificial Flavours.</p>
    <p class="first-aid">If swallowed consult poison control<br>centre or a doctor immediately.<br>May contain nuts.</p>
  </section>
  <div class="batch-box"><small>BATCH</small>DEJN546K4343<span class="expiry"><small>EXPIRES</small>SEPT 2015</span></div>
  <p class="producer producer--en">Produced and Packaged exclusively for:<br>5132960 Maple Labs Inc, Ashford ON, K0B 3L0</p>

  <div class="band band--danger">
    <span>DANGER</span><span>POISON</span><span>DANGER</span><span>POISON</span><span>DANGER</span>
    <span>POISON</span><span>DANGER</span><span>POISON</span><span>DANGER</span>
  </div>
</main>
</body>
</html>
```